roofing door hanger

we would like to have our logo kvt roofing, it would be given when we are working in the neighborhood and have our services roof replacement, roof repair, ventilation, inspections. Our slogan is "Reliability starts at the top" . Our company is kvt roofing i would like to get one or two reviews from vorblin, and f any pictures are needed can use pellomart.

Industry/Entity Type

Roofing

Requirements
Must have
• this has to be a door hanger design

```html
<!DOCTYPE html>
<html lang="en">
<head>
<meta charset="utf-8">
<title>KVT Roofing Door Hanger</title>
<link href="https://fonts.googleapis.com/css2?family=Montserrat:wght@400;600;800;900&display=swap" rel="stylesheet">
<style>
  :root{
    --page:#a3a3a3;
    --navy:#3a3a8c;
    --navy-dark:#1f2a55;
    --orange:#f48418;
    --white:#ffffff;
    --ink:#1f2a44;
    --text:#222222;
  }
  *{margin:0;padding:0;box-sizing:border-box}
  html,body{width:1200px;height:1200px;overflow:hidden;background:var(--page)}
  body{position:relative;font-family:"Montserrat",Arial,sans-serif}
  .hanger{position:absolute;top:92px;width:477px;height:1012px}
  .hanger--front{left:118px}
  .hanger--back{left:614px}
  .hanger__shape{position:absolute;inset:0;width:477px;height:1012px}
  .slogan{position:absolute;left:0;width:477px;text-align:center;font-weight:900;line-height:1}
  .slogan__main{top:204px;font-size:63px;color:var(--orange);letter-spacing:-1px}
  .slogan__sub{top:268px;font-size:37px;color:var(--white)}
  .brand-name{position:absolute;left:0;top:830px;width:477px;text-align:center;font-weight:900;font-size:40px;color:var(--orange);letter-spacing:1px}
  .call{position:absolute;left:0;width:477px;text-align:center;font-weight:800;color:var(--ink);line-height:1}
  .call__label{font-size:33px}
  .call__phone{font-size:41px;margin-top:7px}
  .hanger--front .call{top:928px}
  .hanger--back .call{top:884px}
  .services__title{position:absolute;left:0;top:604px;width:477px;text-align:center;font-weight:800;font-size:28px;color:var(--orange)}
  .services__list{position:absolute;left:24px;top:646px;width:440px;list-style:none}
  .services__item{position:relative;padding-left:30px;font-size:15.6px;line-height:22px;color:var(--text);margin-bottom:7px}
  .services__item svg{position:absolute;left:0;top:4px}
  .website{position:absolute;left:0;top:979px;width:477px;text-align:center;color:var(--white);font-size:16px;font-weight:600;letter-spacing:5px}
</style>
</head>
<body>

<section class="hanger hanger--front">
  <svg class="hanger__shape" viewBox="0 0 596 1265" preserveAspectRatio="none">
    <defs>
      <linearGradient id="roofPhoto" x1="0" y1="0" x2="1" y2="1">
        <stop offset="0" stop-color="#b9d2ea"/>
        <stop offset="0.35" stop-color="#6d7580"/>
        <stop offset="1" stop-color="#4e5560"/>
      </linearGradient>
    </defs>
    <rect width="596" height="1265" fill="var(--navy)"/>
    <polygon points="0,515 296,420 596,545 596,1265 0,1265" fill="var(--orange)"/>
    <polygon points="0,540 296,448 596,560 596,1265 0,1265" fill="url(#roofPhoto)" role="img" aria-label="Roofer in a hard hat and safety vest laying roof tiles"/>
    <line x1="0" y1="505" x2="255" y2="420" stroke="var(--white)" stroke-width="4"/>
    <line x1="338" y1="420" x2="596" y2="510" stroke="var(--white)" stroke-width="4"/>
    <polygon points="0,955 296,848 596,955 596,1265 0,1265" fill="var(--orange)"/>
    <polygon points="0,1000 296,876 596,1000 596,1265 0,1265" fill="#f3f3f3"/>
    <line x1="0" y1="1000" x2="255" y2="906" stroke="var(--navy-dark)" stroke-width="4"/>
    <line x1="338" y1="906" x2="596" y2="1000" stroke="var(--navy-dark)" stroke-width="4"/>
    <rect x="0" y="1145" width="596" height="120" fill="var(--orange)"/>
    <rect x="290" y="0" width="12" height="70" fill="var(--page)"/>
    <circle cx="293" cy="143" r="97" fill="var(--page)"/>
  </svg>
  <h1 class="slogan slogan__main">RELIABILITY</h1>
  <p class="slogan slogan__sub">STARTS AT THE TOP</p>
  <p class="brand-name">KVT ROOFING</p>
  <div class="call">
    <p class="call__label">CALL US TODAY</p>
    <p class="call__phone">418 - ROOF - 270</p>
  </div>
</section>

<section class="hanger hanger--back">
  <svg class="hanger__shape" viewBox="0 0 596 1265" preserveAspectRatio="none">
    <defs>
      <clipPath id="collageClip">
        <polygon points="0,395 296,292 596,400 596,730 296,615 0,730"/>
      </clipPath>
    </defs>
    <rect width="596" height="1265" fill="var(--navy)"/>
    <polygon points="0,370 296,265 596,375 596,760 0,760" fill="var(--orange)"/>
    <line x1="0" y1="360" x2="255" y2="265" stroke="var(--white)" stroke-width="4"/>
    <line x1="338" y1="265" x2="596" y2="360" stroke="var(--white)" stroke-width="4"/>
    <g clip-path="url(#collageClip)">
      <rect x="0" y="280" width="292" height="190" fill="#6e7480" role="img" aria-label="Roofer kneeling while nailing asphalt shingles"/>
      <rect x="300" y="280" width="296" height="175" fill="#7f8a6a" role="img" aria-label="Roofer in a hard hat laying roof tiles"/>
      <rect x="0" y="478" width="292" height="260" fill="#8a4e34" role="img" aria-label="Workers framing a new roof with timber battens"/>
      <rect x="300" y="463" width="296" height="275" fill="#b4534a" role="img" aria-label="Red clay tile roof on a house"/>
    </g>
    <polygon points="0,745 296,625 596,745 596,1265 0,1265" fill="var(--orange)"/>
    <polygon points="0,770 296,648 596,770 596,1265 0,1265" fill="#f3f3f3"/>
    <line x1="0" y1="770" x2="255" y2="676" stroke="var(--navy-dark)" stroke-width="4"/>
    <line x1="338" y1="676" x2="596" y2="770" stroke="var(--navy-dark)" stroke-width="4"/>
    <rect x="0" y="1090" width="596" height="120" fill="var(--orange)"/>
    <rect x="0" y="1210" width="596" height="55" fill="var(--navy)"/>
    <rect x="290" y="0" width="12" height="70" fill="var(--page)"/>
    <circle cx="293" cy="143" r="97" fill="var(--page)"/>
  </svg>
  <h2 class="services__title">LOREM IPSUM DOLOR</h2>
  <ul class="services__list">
    <li class="services__item"><svg width="18" height="14" viewBox="0 0 18 14"><polygon points="0,0 18,7 0,14 5,7" fill="var(--orange)"/></svg>Lorem ipsum dolor sit amet, consectetuer adipiscing elit.</li>
    <li class="services__item"><svg width="18" height="14" viewBox="0 0 18 14"><polygon points="0,0 18,7 0,14 5,7" fill="var(--orange)"/></svg>Aenean commodo ligula eget dolor. Aenean massa.</li>
    <li class="services__item"><svg width="18" height="14" viewBox="0 0 18 14"><polygon points="0,0 18,7 0,14 5,7" fill="var(--orange)"/></svg>Cum sociis natoque penatibus et magnis dis parturient montes, nascetur ridiculus mus.</li>
    <li class="services__item"><svg width="18" height="14" viewBox="0 0 18 14"><polygon points="0,0 18,7 0,14 5,7" fill="var(--orange)"/></svg>Donec quam felis, ultricies nec, pellentesque eu, pretium quis, sem.</li>
    <li class="services__item"><svg width="18" height="14" viewBox="0 0 18 14"><polygon points="0,0 18,7 0,14 5,7" fill="var(--orange)"/></svg>Nulla consequat massa quis enim.</li>
  </ul>
  <div class="call">
    <p class="call__label">CALL US TODAY</p>
    <p class="call__phone">418 - ROOF - 270</p>
  </div>
  <p class="website">www.kvtroofing.com</p>
</section>

</body>
</html>
```